Amber Orchard (instructional dating book)

Title: Amber Orchard
Subtitle: Where to plant tulips along a crooked brick path
Author: R.K. Tolvane
I'm seeking the title to be central with the subtitle underneath and the author slightly lower and to the left. Perhaps a border or two around the font. I thought the background could look aged (off color and old textured paper) and the background slightly punched into the texture like a typewriter has been used. I imagine it something like an old Pemberworth playbook or 1940s morse code manual. Many thanks!

Target Market(s)

18 to 45 year old single people

Industry/Entity Type

Dating

Font styles to use
Serif

Requirements
Must have
• Text with border or two
Nice to have
• Traditional feel. The book is instructional.
Should not have
• Too much color or flair

```html
<!DOCTYPE html>
<html lang="en">
<head>
<meta charset="utf-8">
<title>Amber Orchard — R.K. Tolvane</title>
<link rel="stylesheet" href="https://fonts.googleapis.com/css2?family=Playfair+Display:ital,wght@0,400;0,700;1,400&display=swap">
<style>
  :root {
    --paper: #e8d8c0;
    --paper-edge: #dcc8ab;
    --band: rgba(120, 100, 75, 0.28);
    --ink: #1b1613;
    --emboss: rgba(255, 248, 235, 0.55);
    --ornament: #5a4a3c;
  }
  html, body {
    margin: 0;
    padding: 0;
    overflow: hidden;
    background: var(--paper);
  }
  .cover {
    position: relative;
    width: 857px;
    height: 1200px;
    overflow: hidden;
    background:
      radial-gradient(ellipse at 50% 45%, rgba(255,250,238,0.35) 0%, rgba(255,250,238,0) 60%),
      radial-gradient(ellipse at 50% 50%, var(--paper) 55%, var(--paper-edge) 100%);
    color: var(--ink);
    font-family: "Playfair Display", Georgia, serif;
  }
  .frame {
    position: absolute;
    inset: 0;
  }
  .title-band {
    position: absolute;
    left: 0;
    top: 152px;
    width: 857px;
    height: 408px;
    background: var(--band);
  }
  .title {
    position: absolute;
    left: 0;
    top: 178px;
    width: 857px;
    margin: 0;
    text-align: center;
    font-weight: 400;
    font-size: 150px;
    line-height: 172px;
    text-transform: uppercase;
    text-shadow: 0 2px 1px var(--emboss), 0 -1px 0 rgba(0,0,0,0.25);
  }
  .title-line {
    display: block;
  }
  .title-line--first {
    letter-spacing: 30px;
    padding-left: 30px;
  }
  .title-line--second {
    letter-spacing: 4px;
    font-size: 132px;
  }
  .rule {
    position: absolute;
    left: 148px;
    width: 562px;
    height: 2px;
    background: var(--ink);
  }
  .rule--top { top: 649px; }
  .rule--bottom { top: 879px; }
  .subtitle {
    position: absolute;
    left: 148px;
    top: 696px;
    width: 562px;
    margin: 0;
    text-align: center;
    font-style: italic;
    font-weight: 400;
    font-size: 38px;
    line-height: 64px;
    letter-spacing: 2.5px;
    text-shadow: 0 1px 1px var(--emboss);
  }
  .ornament {
    position: absolute;
    left: 368px;
    top: 962px;
    width: 120px;
    height: 22px;
    border-radius: 11px;
    background: linear-gradient(90deg, rgba(90,74,60,0) 0%, var(--ornament) 50%, rgba(90,74,60,0) 100%);
    opacity: 0.55;
  }
  .author {
    position: absolute;
    left: 0;
    top: 1030px;
    width: 857px;
    margin: 0;
    text-align: center;
    font-weight: 700;
    font-size: 34px;
    line-height: 50px;
    text-shadow: 0 1px 1px var(--emboss);
  }
</style>
</head>
<body>
  <main class="cover">
    <div class="title-band"></div>
    <svg class="frame" width="857" height="1200" viewBox="0 0 857 1200" aria-hidden="true">
      <rect x="30" y="30" width="797" height="1140" fill="none" stroke="#1b1613" stroke-width="2"/>
      <rect x="39" y="39" width="779" height="1122" fill="none" stroke="#1b1613" stroke-width="2"/>
    </svg>
    <h1 class="title">
      <span class="title-line title-line--first">Amber</span>
      <span class="title-line title-line--second">Orchard</span>
    </h1>
    <div class="rule rule--top"></div>
    <p class="subtitle">Where to plant tulips along a crooked brick path</p>
    <div class="rule rule--bottom"></div>
    <div class="ornament" role="img" aria-label="Small calligraphic flourish ornament"></div>
    <p class="author">R.K. Tolvane</p>
  </main>
</body>
</html>
```